Sam Greenfield Billboard

**Task Description: Billboard Design for Self Storage Facility**

**Objective:**
Design a captivating billboard to promote our self-storage facility with a focus on our convenient location and online rental capabilities.

**Key Messages to Include:**
1. **Location Emphasis:** Highlight that our facility is located right beside the billboard (maybe by using an arrow pointing left).
2. **Online Rental Convenience:** Feature prominently that customers can "Rent Online Anytime!” or that we are "Always Open Online!"

**Target Audience:**
- Local residents looking for convenient self-storage solutions.
- Businesses needing storage space accessible around the clock.

**Design Elements:**
1. **Visual Impact:** Eye-catching graphics and colors that stand out against the surroundings.
2. **Clear Text:** Bold and concise messaging that can be read and understood quickly.
3. **Contact Information:** Include our phone number and website URL for easy access to further information.

**Additional Information:**
- Billboard dimensions: 12 ft. x 24 ft.
- Preferred color scheme: Bright and attention-grabbing, but professional.
- Branding: Incorporate our logo and brand colors to maintain consistency.

**Deliverables:**
- High-resolution digital file compatible with billboard printing specifications.
- Consider mockups or visualizations for presentation purposes.

Please note that I have attached current logos/graphics that we would love to incorporate into the billboard as well as a picture of our current billboard. Our logo (Sam Greenfield Self Storage - SG navy.png) MUST be incorporated into the billboard. Also feel free to add any of the current descriptions from the picture of our current billboard into the design. Instead of using "Climate Controlled" use "Temperature Controlled". Thank you for your attention to these details. We look forward to reviewing your proposed design!

```html
<!DOCTYPE html>
<html lang="en">
<head>
<meta charset="utf-8">
<title>Sam Greenfield Self Storage Billboard</title>
<link rel="stylesheet" href="https://fonts.googleapis.com/css2?family=Montserrat:wght@500;600;700;800&family=Roboto:ital,wght@0,700;1,700;1,900&display=swap">
<style>
  :root {
    --page: #eceeef;
    --board-grey: #cdcfce;
    --navy: #1d2b5a;
    --navy-deep: #141f45;
    --tan: #a88754;
    --gold: #f2b21c;
    --tick: #e8a91a;
    --white: #ffffff;
    --device: #1b1d22;
    --screen-top: #e9edf4;
    --screen-bottom: #8a9bb8;
  }
  * { margin: 0; padding: 0; box-sizing: border-box; }
  html, body { width: 1200px; height: 1000px; overflow: hidden; background: var(--page); }
  .billboard {
    position: absolute; left: 40px; top: 200px;
    width: 1120px; height: 600px;
    background: var(--board-grey);
    overflow: hidden;
    font-family: "Montserrat", sans-serif;
    color: var(--navy);
  }
  .billboard-shapes { position: absolute; inset: 0; }
  .brand-mark {
    position: absolute; left: 34px; top: 72px;
    display: flex; align-items: center; gap: 8px;
    font-family: "Montserrat", sans-serif; font-weight: 700;
    font-size: 15px; letter-spacing: 0.5px; color: var(--navy);
  }
  .brand-mark .square { width: 14px; height: 14px; background: var(--navy); }
  .headline { position: absolute; left: 114px; top: 132px; line-height: 1; }
  .headline .name { display: block; font-weight: 500; font-size: 41px; letter-spacing: 0.5px; }
  .headline .service { display: block; font-weight: 800; font-size: 56px; margin-top: 6px; letter-spacing: 0.5px; }
  .features { position: absolute; left: 114px; top: 280px; list-style: none; }
  .features li {
    display: flex; align-items: center; gap: 8px;
    font-weight: 500; font-size: 27px; height: 42px; letter-spacing: 0.3px;
  }
  .features svg { width: 24px; height: 24px; flex: none; }
  .address {
    position: absolute; left: 84px; top: 460px;
    font-family: "Roboto", sans-serif; font-style: italic; font-weight: 900;
    font-size: 31px; color: var(--navy); letter-spacing: 0.3px;
  }
  .website {
    position: absolute; left: 122px; top: 546px;
    display: flex; align-items: center; gap: 10px;
    font-family: "Roboto", sans-serif; font-weight: 700; font-size: 27px; color: var(--navy);
  }
  .website svg { width: 28px; height: 28px; }
  .tagline {
    position: absolute; left: 802px; top: 62px;
    font-family: "Roboto", sans-serif; font-style: italic; font-weight: 700;
    font-size: 42px; line-height: 1.12; color: var(--white);
  }
  .phone {
    position: absolute; left: 800px; top: 522px;
    display: flex; align-items: center; gap: 12px;
    font-family: "Roboto", sans-serif; font-weight: 700; font-size: 33px; color: var(--white);
    letter-spacing: 0.5px;
  }
  .phone svg { width: 24px; height: 24px; }
  .device {
    position: absolute; background: var(--device);
    border-radius: 10px; padding: 6px;
    box-shadow: 0 4px 10px rgba(0,0,0,0.35);
  }
  .device .screen {
    width: 100%; height: 100%; border-radius: 4px;
    background: linear-gradient(180deg, var(--screen-top) 0%, var(--screen-bottom) 45%, var(--screen-top) 100%);
  }
  .device.tablet-main { left: 674px; top: 193px; width: 266px; height: 227px; }
  .device.tablet-side { left: 946px; top: 176px; width: 115px; height: 235px; }
  .device.tablet-side .screen { background: linear-gradient(180deg, var(--navy) 0%, var(--screen-top) 40%, var(--screen-top) 100%); }
  .device.phone-handset { left: 658px; top: 273px; width: 55px; height: 176px; border-radius: 9px; padding: 4px; }
  .device.phone-handset .screen { background: linear-gradient(180deg, var(--navy) 0%, var(--screen-bottom) 60%, var(--screen-top) 100%); }
</style>
</head>
<body>
<main class="billboard">
  <svg class="billboard-shapes" viewBox="0 0 1120 600" width="1120" height="600" aria-hidden="true">
    <defs>
      <linearGradient id="panelShade" x1="0" y1="0" x2="1" y2="1">
        <stop offset="0" stop-color="#24356a"/>
        <stop offset="1" stop-color="#121b3d"/>
      </linearGradient>
    </defs>
    <rect class="side-panel" x="757" y="0" width="363" height="600" fill="url(#panelShade)" role="img" aria-label="Dark blue photo of storage unit doors"/>
    <polygon class="tan-band" points="757,160 915,0 1120,0 1120,185 757,225" fill="var(--tan)"/>
    <path class="gold-swoosh" d="M89,440 C300,432 560,405 680,332 C752,282 762,150 747,0 L777,0 C792,150 784,305 722,382 C622,482 300,530 89,535 Z" fill="var(--gold)"/>
    <polygon class="gold-arrowhead" points="13,488 92,410 92,566" fill="var(--gold)"/>
  </svg>

  <div class="brand-mark"><span class="square"></span>SAM GREENFIELD</div>

  <h1 class="headline">
    <span class="name">SAM GREENFIELD</span>
    <span class="service">SELF STORAGE</span>
  </h1>

  <ul class="features">
    <li><svg viewBox="0 0 24 24"><path d="M3 13 L9 19 L21 5" fill="none" stroke="var(--tick)" stroke-width="3.5" stroke-linecap="round" stroke-linejoin="round"/></svg>LARGE/SMALL UNITS</li>
    <li><svg viewBox="0 0 24 24"><path d="M3 13 L9 19 L21 5" fill="none" stroke="var(--tick)" stroke-width="3.5" stroke-linecap="round" stroke-linejoin="round"/></svg>TEMPERATURE CONTROLLED</li>
    <li><svg viewBox="0 0 24 24"><path d="M3 13 L9 19 L21 5" fill="none" stroke="var(--tick)" stroke-width="3.5" stroke-linecap="round" stroke-linejoin="round"/></svg>COVERED BOAT/RV PARKING</li>
  </ul>

  <p class="address">218 MAPLE RIDGE DRIVE</p>

  <p class="website">
    <svg viewBox="0 0 24 24"><g fill="none" stroke="var(--navy)" stroke-width="1.8"><circle cx="12" cy="12" r="10"/><ellipse cx="12" cy="12" rx="4.5" ry="10"/><path d="M2 12 H22 M4 6.5 H20 M4 17.5 H20"/></g></svg>
    www.SamGreenfieldStorage.com
  </p>

  <p class="tagline">Rent online<br>anytime!</p>

  <div class="device phone-handset" role="img" aria-label="Phone showing the online rental website"><div class="screen"></div></div>
  <div class="device tablet-main" role="img" aria-label="Tablet showing the online rental website home page"><div class="screen"></div></div>
  <div class="device tablet-side" role="img" aria-label="Tablet showing available storage units"><div class="screen"></div></div>

  <p class="phone">
    <svg viewBox="0 0 24 24"><path d="M6.6 10.8c1.4 2.8 3.8 5.2 6.6 6.6l2.2-2.2c.3-.3.7-.4 1-.2 1.1.4 2.3.6 3.6.6.6 0 1 .4 1 1V20c0 .6-.4 1-1 1C10.6 21 3 13.4 3 4c0-.6.4-1 1-1h3.5c.6 0 1 .4 1 1 0 1.3.2 2.5.6 3.6.1.3 0 .7-.2 1L6.6 10.8z" fill="var(--white)"/></svg>
    555 301 4826
  </p>
</main>
</body>
</html>
```